Cover-Design für Buchprojekt
kiwano suchte ein neues Design in der Kategorie Buch-/eBook-Cover und hat ein Projekt auf entwurfsbuero.de gestartet.
Das sagt der Auftraggeber
Vielen Dank für das wunderbare, moderne Design unseres Buchcovers. Ihre Freundlichkeit, Schnelligkeit und Geduld bei der Ausarbeitung war sehr professionell. Wir empfehlen Sie gerne weiter und speichern Ihr Profil für das nächste Projekt. kiwano
Zielgruppe
Wir benötigen ein Cover für ein Buchprojekt, in dem es um Geld sparen für Kinder in Aktien/ETFs geht.
Eltern/Großeltern/Onkel/Tanten möchten Geld ansparen für ihr Kind, wissen aber, dass ein Sparbuch heutzutage aufgrund der niedrigen Zinsen keine gute Möglichkeit ist, haben schon von ETFs gehört (oder legen selber an) und möchten nun auch ein Depot für ihr Kind (Enkelkind, Nichte, Neffe) anlegen.
Zielgruppe:
1. Eltern (eher Mütter), die sich bereits selbst mit dem Thema Geldanlage beschäftigt haben, die selbst bereits ein ETF-Depot zur Altersvorsorge haben und nun überlegen, wie sie für ihr Kind/Kinder diese Vorteile auch nutzen können.
2 Eltern, bei denen Verwandte (Großeltern/Tanten/Onkel) den Wunsch haben, für die Kinder Geld anzusparen für die Zukunft. Doch diese möchten in einen Aktienfonds bei der Bank investieren, die Eltern kennen sich mit modernen Formen der Geldanlage aus und finden es sinnvoller, einen ETF-Depot fürs Kind einzurichten. Nun möchten sie die Verwandten mit diesem Buch davon überzeugen.
- Welche Probleme und Herausforderungen hat diese Zielgruppe?
Sie sind finanziell recht stabil aufgestellt und machen sich nun Gedanken um die Zukunft ihrer Kinder. Als Sicherheit möchten sie auch für ihre Kinder sparen. Sei es, um später mal ein Studium/Ausbildung zu finanzieren (eine „gute“ Ausbildung, womöglich auch ein Auslandssemester zu ermöglichen), den Führerschein, die erste eigene Wohnung oder einfach nur als Finanzpolster, wenn mal „was passiert“.
- Welche Ziele verfolgt deine Zielgruppe?
Sie möchten Sicherheit und Wohlstand für ihre Kinder/Enkel.
Sie möchten trotz Niedrigzinsumfeld das Geld fürs Kind sicher und gewinnbringend in ETFs anlegen.
Aufgabenstellung
Hochwertiges, modernes, minimalistisches Design, das sich von der Masse abhebt. Keine Aktiencharts. Keine Pflanzen, die wachsen oder gegossen werden. Gerne ein Design, das Sicherheit fürs Kind vermittelt (kein Muss). Keine Personen frontal. Wirkung wie ein seriöser Ratgeber (z.B. wie Ratgeber vom RT Verlag oder PW).
Autor: Konstantin Brugger
Titel/Untertitel: Unser Nachwuchs baut früh Vermögen auf. Wie Eltern sicher in ETFs sparen, Fallstricke von Anfang an vermeiden und ein Geld-Mindset prägen
Backcover und Buchrücken wird benötigt (dies erst im nächsten Schritt, Backcovertext wird dann gegeben)
Format Taschenbuch: 5x8

```html
<!DOCTYPE html>
<html lang="de">
<head>
<meta charset="utf-8">
<title>Das Kinder Konto – Buchcover</title>
<link rel="stylesheet" href="https://fonts.googleapis.com/css2?family=Nunito+Sans:wght@800&family=Encode+Sans+Condensed:wght@400&family=Fira+Sans:wght@500&display=swap">
<style>
  :root {
    --stage: #363636;
    --cover-top: #44525e;
    --cover-mid: #2b3a47;
    --cover-bottom: #1a2733;
    --text-white: #ffffff;
    --text-soft: #eef1f4;
  }
  * { margin: 0; padding: 0; box-sizing: border-box; }
  html, body {
    width: 1200px;
    height: 800px;
    overflow: hidden;
    background: var(--stage);
  }
  .stage {
    width: 1200px;
    height: 800px;
    display: flex;
    align-items: center;
    justify-content: center;
  }
  .book-cover {
    position: relative;
    width: 450px;
    height: 720px;
    background: linear-gradient(180deg, var(--cover-top) 0%, var(--cover-mid) 45%, var(--cover-bottom) 100%);
    color: var(--text-white);
  }
  .title-block {
    position: absolute;
    top: 170px;
    left: 55px;
    width: 330px;
    font-family: "Nunito Sans", sans-serif;
    font-weight: 800;
    color: var(--text-white);
  }
  .title-article {
    display: block;
    font-size: 34px;
    line-height: 1;
    margin-left: 110px;
  }
  .title-main {
    display: block;
    font-size: 72px;
    line-height: 1;
    letter-spacing: -1px;
    margin-top: 2px;
  }
  .title-sub {
    display: block;
    text-align: right;
    font-size: 50px;
    line-height: 1;
    letter-spacing: -1px;
    margin-top: 8px;
  }
  .subtitle {
    position: absolute;
    top: 420px;
    left: 30px;
    right: 30px;
    text-align: center;
    font-family: "Encode Sans Condensed", sans-serif;
    font-size: 17px;
    line-height: 28px;
    color: var(--text-soft);
  }
  .author {
    position: absolute;
    bottom: 40px;
    left: 0;
    right: 0;
    text-align: center;
    font-family: "Fira Sans", sans-serif;
    font-weight: 500;
    font-size: 20px;
    letter-spacing: 2px;
    color: var(--text-white);
  }
</style>
</head>
<body>
  <main class="stage">
    <article class="book-cover">
      <h1 class="title-block">
        <span class="title-article">Das</span>
        <span class="title-main">KINDER</span>
        <span class="title-sub">KONTO</span>
      </h1>
      <p class="subtitle">Wie Eltern sicher in ETFs sparen,<br>Fallstricke von Anfang an vermeiden und ein<br>Geld-Mindset prägen</p>
      <p class="author">Konstantin Brugger</p>
    </article>
  </main>
</body>
</html>
```